Business Card Design needed for logo design project

This project is linked to Logo: brand identity for modern furniture design studio..

Our company needs a Business Card Design. Please refer to our original project in the link above.

Industry/Entity Type

Business

```html
<!DOCTYPE html>
<html lang="en">
<head>
<meta charset="utf-8">
<title>Corvana Business Card</title>
<link rel="stylesheet" href="https://fonts.googleapis.com/css2?family=Quicksand:wght@300;400;500;600&display=swap">
<style>
  :root {
    --page-bg: #e4e5e6;
    --card-white: #f7f7f6;
    --band-grey: #b8bab8;
    --ink: #3f4144;
    --ink-soft: #55585b;
    --back-dark: #2c3237;
    --back-mid: #4f5c64;
    --back-light: #8197a1;
    --back-mark: #323a40;
  }
  * { box-sizing: border-box; margin: 0; padding: 0; }
  html, body {
    width: 1200px;
    height: 1000px;
    overflow: hidden;
    background: var(--page-bg);
    font-family: "Quicksand", sans-serif;
  }
  .card {
    position: absolute;
    left: 250px;
    width: 700px;
    height: 400px;
    border-radius: 3px;
    box-shadow: 0 6px 18px rgba(0,0,0,0.12);
    overflow: hidden;
  }
  .card-front {
    top: 70px;
    background: var(--card-white);
  }
  .side-band {
    position: absolute;
    top: 0;
    width: 62px;
    height: 100%;
    background: var(--band-grey);
  }
  .side-band.left { left: 0; }
  .side-band.right { right: 0; }
  .brand-name {
    position: absolute;
    font-weight: 300;
    color: var(--ink);
    letter-spacing: 2px;
    line-height: 1;
  }
  .card-front .brand-name {
    left: 100px;
    top: 48px;
    font-size: 104px;
  }
  .contact-block {
    position: absolute;
    left: 330px;
    top: 212px;
    color: var(--ink);
  }
  .person-name {
    font-size: 25px;
    font-weight: 400;
    letter-spacing: 0.5px;
    line-height: 1;
  }
  .person-role {
    font-size: 11px;
    font-weight: 600;
    color: var(--ink-soft);
    margin-top: 3px;
    margin-bottom: 16px;
  }
  .contact-list { list-style: none; }
  .contact-list li {
    display: flex;
    align-items: center;
    gap: 10px;
    font-size: 20px;
    font-weight: 400;
    line-height: 1;
    margin-bottom: 10px;
  }
  .contact-icon {
    width: 13px;
    height: 13px;
    flex: none;
    fill: var(--ink-soft);
  }
  .card-back {
    top: 530px;
    background: linear-gradient(135deg, var(--back-dark) 0%, var(--back-mid) 50%, var(--back-light) 100%);
  }
  .card-back .brand-name {
    left: 0;
    right: 0;
    top: 146px;
    text-align: center;
    font-size: 96px;
    color: var(--back-mark);
  }
</style>
</head>
<body>
  <section class="card card-front" aria-label="Business card front">
    <div class="side-band left"></div>
    <div class="side-band right"></div>
    <div class="brand-name">corvana</div>
    <div class="contact-block">
      <div class="person-name">YOUR NAME</div>
      <div class="person-role">Designation</div>
      <ul class="contact-list">
        <li>
          <svg class="contact-icon" viewBox="0 0 16 16"><path d="M8 1 1 7.5h2V15h4v-4h2v4h4V7.5h2z"/></svg>
          <span>123 Avenue XYZ, 12345</span>
        </li>
        <li>
          <svg class="contact-icon" viewBox="0 0 16 16"><path d="M4 1h3l1 4-2 1.2a8 8 0 0 0 3.8 3.8L11 8l4 1v3a2 2 0 0 1-2 2C7 14 2 9 2 3a2 2 0 0 1 2-2z"/></svg>
          <span>000 . 1234 .5678</span>
        </li>
        <li>
          <svg class="contact-icon" viewBox="0 0 16 16"><path d="M1 3h14v10H1zm1.5 1.2L8 8.6l5.5-4.4z"/></svg>
          <span>name@email.com</span>
        </li>
        <li>
          <svg class="contact-icon" viewBox="0 0 16 16"><circle cx="8" cy="8" r="7"/><path d="M1 8h14M8 1c-3 3.5-3 10.5 0 14M8 1c3 3.5 3 10.5 0 14" stroke="#f7f7f6" stroke-width="1" fill="none"/></svg>
          <span>mywebsite.com</span>
        </li>
      </ul>
    </div>
  </section>

  <section class="card card-back" aria-label="Business card back">
    <div class="brand-name">corvana</div>
  </section>
</body>
</html>
```